Dental Savings Plan - Marcus Pelligrew DDS

We need a tri-fold brochure and 1 page flyer/poster for Dr. Marcus Pelligrew' dental office located on Maui, Hawaii. We are offering a new "Dental Savings Plan" to patients.
I have included 3 photos, along with the office logo. You do not have to use all photos if you do not want to. We want this to catch the eyes of patients, easy for them to read and understand, and to show them that this is a much better option than dental insurance.
Please use same Hawaiian theme and colors on the office website https://www.brightreefdental.com .

Please also include the following to promote this new plan:

Dental Services Include
• Professional Dental Cleanings (2 per benefit year)
• Perio Maintenance Cleanings (3 per benefit year) covered at 80%
• Radiographs as needed (1 set of X-rays per benefit year)
• Doctor Examinations (2 per benefit year)
• Ozone Treatment
• PRISM Amalgam Removal
• Additional limited/emergency exam (1 per benefit year)
• Cosmetic consultation
• 15% discount on all other services (including cosmetic procedures)
• 10% discount on implants and implant crowns

Advantages of the Dental Savings Plan
1. No deductibles
2. No waiting periods
3. No claims to file
4. No frequency limitations or exclusions
5. No yearly maximum benefits
6. No pre-authorization requirements
7. No pre-existing conditions limitations
8. State of the art facility and technology
9. Immediate enrollment
10. Highest quality of care for you and your Ohana

Annual Fee
$399 first family member/individual (equivalent to $33 per month)
$349 second family member (equivalent to $29 per month)
$249 each additional family member (equivalent to $20 per month)

Provisions of the Dental Savings Plan
• May not be combined with insurance plans, discounts or promotions
• This Dental Savings Plan is not an insurance plan, but a payment arrangement provided by Marcus Pelligrew DDS, and is not transferable to any other dental office or dental specialist
• Payment for services are due at the date of service
• This program is for you and is not transferable
• Benefits are provided for one year from the date the plan is purchased
• Must be paid in full when starting the plan
• No refunds will be provided for dues of the plan annual fee under any circumstances, including failure to schedule and maintain appointments
• If Paywell Finance is used to pay for the program and for services then only a 10% discount will be given
• To receive the full 15% discount on restorative treatment, you must schedule the appointment the day it is recommended. Any failed appointment results in the loss of the 15% discount.

Target Market(s)

Dental patients without dental insurance

Industry/Entity Type

Dental Clinic

Requirements
Must have
• My project must have the logo file to identify the dental office, Hawaiian theme, same colors as website, match style of website font, theme and colors, as well as, all the Dental Services, Advantages of the Dental Savings Plan, Annual Fee, and the Provisions of the Dental Savings Plan.

```html
<!DOCTYPE html>
<html lang="en">
<head>
<meta charset="utf-8">
<title>Dental Savings Plan – Tri-fold Brochure</title>
<link href="https://fonts.googleapis.com/css2?family=Raleway:wght@400;500;600;700&family=Oswald:wght@500&family=Cinzel:wght@500&display=swap" rel="stylesheet">
<style>
  :root {
    --green: #4aab35;
    --green-bright: #22c24c;
    --black: #1c1c1c;
    --white: #ffffff;
    --blue-wave: #1fa3dc;
    --ocean-deep: #0f7fb8;
    --ocean-light: #2fc0de;
    --phone-blue: #1f5fae;
    --backdrop: #4d4642;
  }
  * { box-sizing: border-box; margin: 0; padding: 0; }
  html, body { width: 1200px; height: 1200px; overflow: hidden; background: var(--backdrop); }
  .stage { position: absolute; left: 0; top: 0; width: 1500px; height: 1500px; transform: scale(0.8); transform-origin: 0 0; font-family: "Raleway", sans-serif; }
  .sheet { position: absolute; overflow: hidden; box-shadow: 0 6px 18px rgba(0,0,0,.35); }
  .sheet svg.art { position: absolute; inset: 0; width: 100%; height: 100%; }
  .sheet-inside { left: 80px; top: 100px; width: 700px; height: 541px; }
  .sheet-outside { left: 724px; top: 683px; width: 701px; height: 540px; }
  .abs { position: absolute; }

  /* inside: advantages */
  .advantages { left: 8px; top: 214px; width: 222px; color: var(--white); }
  .panel-title { font-weight: 600; font-size: 12.5px; line-height: 14px; text-align: center; margin-bottom: 6px; }
  .advantages ol { list-style: none; font-size: 10.6px; line-height: 12.7px; }

  /* inside: annual fee */
  .fee-title { left: 305px; top: 339px; color: var(--white); font-size: 15px; font-weight: 500; }
  .fee-table { left: 240px; top: 362px; width: 210px; }
  .fee-row { display: flex; height: 30px; margin-bottom: 1px; }
  .fee-price { width: 68px; background: var(--green-bright); color: var(--white); font-size: 13px; font-weight: 500; display: flex; align-items: center; justify-content: center; }
  .fee-desc { flex: 1; background: rgba(25, 190, 170, .55); color: var(--white); font-size: 8.6px; line-height: 10.5px; padding: 2px 3px; }

  /* inside: provisions */
  .provisions { left: 489px; top: 134px; width: 208px; color: var(--white); }
  .provisions .panel-title { text-align: left; font-size: 11px; margin-bottom: 4px; }
  .provisions ul { list-style: none; font-size: 8.3px; line-height: 10.5px; }
  .provisions li { position: relative; padding-left: 2px; margin-bottom: 4.3px; }
  .provisions li::before { content: "•"; position: absolute; left: -12px; }

  /* outside: services */
  .services { left: 20px; top: 93px; width: 200px; color: var(--white); }
  .services .panel-title { font-size: 12.5px; margin-bottom: 16px; padding-left: 12px; }
  .services ul { list-style: none; font-size: 10.6px; line-height: 12.8px; }
  .services li { position: relative; padding-left: 18px; margin-bottom: 2px; }
  .services li::before { content: "•"; position: absolute; left: 0; font-size: 8px; }

  /* outside: contact */
  .brand-name { left: 398px; top: 112px; color: var(--white); font-size: 11px; font-weight: 700; display: flex; align-items: center; gap: 5px; }
  .brand-name .dot { width: 9px; height: 9px; border-radius: 50%; background: var(--green); }
  .doctor-name { left: 254px; top: 294px; color: var(--green); font-weight: 700; font-size: 15px; letter-spacing: .2px; }
  .contact-pill { left: 251px; top: 352px; width: 196px; height: 41px; border-radius: 14px; background: var(--green); color: var(--white); font-weight: 600; font-size: 18px; display: flex; align-items: center; justify-content: center; }
  .contact-details { left: 240px; top: 414px; width: 218px; text-align: center; color: var(--black); font-size: 10px; line-height: 13px; }
  .phone { font-family: "Oswald", sans-serif; color: var(--phone-blue); font-size: 20px; line-height: 24px; }
  .address { display: flex; align-items: center; justify-content: center; gap: 3px; margin-top: 2px; }
  .plan-title { left: 520px; top: 452px; width: 110px; text-align: center; font-family: "Cinzel", serif; font-size: 19px; line-height: 20px; }
  .plan-title .g { color: var(--green); }
  .plan-title .k { color: var(--black); }
</style>
</head>
<body>
<main class="stage">

  <!-- Inside spread -->
  <section class="sheet sheet-inside">
    <svg class="art" viewBox="0 0 700 541" preserveAspectRatio="none">
      <defs>
        <linearGradient id="oceanTop" x1="0" y1="0" x2="0" y2="1">
          <stop offset="0" stop-color="#0d6fa8"/><stop offset="1" stop-color="#24b8dc"/>
        </linearGradient>
        <linearGradient id="palmSky" x1="0" y1="0" x2="0" y2="1">
          <stop offset="0" stop-color="#7fc6ee"/><stop offset=".45" stop-color="#5db0e0"/><stop offset=".6" stop-color="#1a9bcf"/><stop offset="1" stop-color="#23b3c9"/>
        </linearGradient>
      </defs>
      <rect width="700" height="541" fill="var(--green)"/>
      <path role="img" aria-label="Turquoise tropical sea with a palm trunk" d="M0,0 H700 V40 C640,70 580,110 500,110 C430,110 380,70 300,60 C200,50 100,95 0,120 Z" fill="url(#oceanTop)"/>
      <rect role="img" aria-label="Palm tree against blue sky over the ocean" x="234" y="95" width="233" height="420" fill="url(#palmSky)"/>
      <path d="M0,120 C100,95 200,50 300,60 C380,70 430,110 500,110 C580,110 640,70 700,40 V80 C640,108 580,122 500,120 C420,118 380,100 300,96 C200,92 100,130 0,160 Z" fill="var(--black)"/>
      <path d="M0,488 C150,512 300,500 450,468 C560,444 640,428 700,428 V541 H0 Z" fill="var(--blue-wave)"/>
      <path d="M0,493 C100,522 210,532 330,522 C460,511 590,478 700,470 V541 H0 Z" fill="var(--black)"/>
      <path d="M0,500 C80,527 180,540 300,541 H0 Z" fill="var(--green)"/>
    </svg>

    <div class="abs advantages">
      <h2 class="panel-title">Advantages of the Dental Savings Plan</h2>
      <ol>
        <li>1. No deductibles</li>
        <li>2. No waiting periods</li>
        <li>3. No claims to file</li>
        <li>4. No frequency limitations or exclusions</li>
        <li>5. No yearly maximum benefits</li>
        <li>6. No pre-authorization requirements</li>
        <li>7. No pre-existing conditions limitations</li>
        <li>8. State of the art facility and technology</li>
        <li>9. Immediate enrollment</li>
        <li>10. Highest quality of care for you and your Ohana</li>
      </ol>
    </div>

    <h2 class="abs fee-title">Annual Fee</h2>
    <div class="abs fee-table">
      <div class="fee-row"><div class="fee-price">$399</div><div class="fee-desc">first family member/individual (equivalent to $33 per month)</div></div>
      <div class="fee-row"><div class="fee-price">$349</div><div class="fee-desc">second family member (equivalent to $29 per month)</div></div>
      <div class="fee-row"><div class="fee-price">$249</div><div class="fee-desc">each additional family member (equivalent to $20 per month)</div></div>
    </div>

    <div class="abs provisions">
      <h2 class="panel-title">Provisions of the Dental Savings Plan</h2>
      <ul>
        <li>May not be combined with insurance plans, discounts or promotions</li>
        <li>This Dental Savings Plan is not an insurance plan, but a payment arrangement provided by Marcus Pelligrew DDS, and is not transferable to any other dental office or dental specialist</li>
        <li>Payment for services are due at the date of service</li>
        <li>This program is for you and is not transferable</li>
        <li>Benefits are provided for one year from the date the plan is purchased</li>
        <li>Must be paid in full when starting the plan</li>
        <li>No refunds will be provided for dues of the plan annual fee under any circumstances, including failure to schedule and maintain appointments</li>
        <li>If Paywell Finance is used to pay for the program and for services then only a 10% discount will be given</li>
        <li>To receive the full 15% discount on restorative treatment, you must schedule the appointment the day it is recommended. Any failed appointment results in the loss of the 15% discount.</li>
      </ul>
    </div>
  </section>

  <!-- Outside spread -->
  <section class="sheet sheet-outside">
    <svg class="art" viewBox="0 0 701 540" preserveAspectRatio="none">
      <defs>
        <linearGradient id="beach" x1="0" y1="0" x2="0" y2="1">
          <stop offset="0" stop-color="#8fd0f2"/><stop offset=".38" stop-color="#3fb6d8"/><stop offset=".62" stop-color="#2bb3c4"/><stop offset=".75" stop-color="#e9f3f0"/><stop offset="1" stop-color="#e3a862"/>
        </linearGradient>
        <linearGradient id="cornerSea" x1="0" y1="0" x2="0" y2="1">
          <stop offset="0" stop-color="#8ccdf0"/><stop offset="1" stop-color="#1a9ccc"/>
        </linearGradient>
        <radialGradient id="portrait" cx=".5" cy=".45" r=".6">
          <stop offset="0" stop-color="#d9c2ad"/><stop offset="1" stop-color="#8aa6b8"/>
        </radialGradient>
      </defs>
      <rect width="701" height="540" fill="var(--white)"/>
      <rect width="234" height="540" fill="var(--green)"/>
      <path role="img" aria-label="Tropical beach with palm fronds, turquoise water and sand" d="M225,0 H701 V390 C610,325 520,245 430,195 C330,140 260,75 225,0 Z" fill="url(#beach)"/>
      <path d="M225,0 C260,75 330,140 430,195 C520,245 610,325 701,390 V400 C620,340 530,275 440,225 C340,170 260,95 232,0 Z" fill="var(--green)"/>
      <path d="M232,0 C260,95 340,170 440,225 C560,295 640,400 660,540 H690 C680,400 610,290 470,215 C360,155 285,85 262,0 Z" fill="var(--green)"/>
      <path d="M232,0 C255,90 330,165 430,222 C545,287 625,390 652,540 H678 C660,400 590,290 460,222 C350,160 280,85 250,0 Z" fill="var(--black)"/>
      <path role="img" aria-label="Ocean horizon and palm trunk" d="M0,390 C40,445 90,500 122,540 H0 Z" fill="url(#cornerSea)"/>
      <path d="M0,365 C50,425 105,485 135,540 H122 C90,500 40,445 0,390 Z" fill="var(--black)"/>
      <circle cx="356" cy="222" r="51" fill="#dfe3e6"/>
      <circle role="img" aria-label="Portrait photo of the dentist" cx="356" cy="222" r="46" fill="url(#portrait)"/>
    </svg>

    <div class="abs services">
      <h2 class="panel-title">Dental Services Include</h2>
      <ul>
        <li>Professional Dental Cleanings (2 per benefit year)</li>
        <li>Perio Maintenance Cleanings (3 per benefit year) covered at 80%</li>
        <li>Radiographs as needed (1 set of X-rays per benefit year)</li>
        <li>Doctor Examinations (2 per benefit year)</li>
        <li>Ozone Treatment</li>
        <li>PRISM Amalgam Removal</li>
        <li>Additional limited/emergency exam (1 per benefit year)</li>
        <li>Cosmetic consultation</li>
        <li>15% discount on all other services (including cosmetic procedures)</li>
        <li>10% discount on implants and implant crowns</li>
      </ul>
    </div>

    <div class="abs brand-name"><span class="dot"></span>Bright Reef Dental</div>
    <h1 class="abs doctor-name">MARCUS PELLIGREW DDS</h1>
    <div class="abs contact-pill">CONTACT US:</div>
    <div class="abs contact-details">
      <div class="phone">808-555-0172</div>
      <div>www.brightreefdental.com</div>
      <div>hello@brightreefdental.com</div>
      <div class="address">
        <svg width="10" height="10" viewBox="0 0 10 10" aria-hidden="true"><path d="M1,5 L5,1 L9,5 V9 H6 V6 H4 V9 H1 Z" fill="var(--black)"/></svg>
        <span>455 MAKAI LOOP # 112, KIHEI, HI 96799</span>
      </div>
    </div>
    <div class="abs plan-title"><div class="g">DENTAL</div><div class="k">SAVING</div><div class="g">PLAN</div></div>
  </section>

</main>
</body>
</html>
```